Trelvane Summit Flyer to describe services

I provide data abstraction and consulting services to hospitals that are participating in an accreditation program for their bariatric surgery program. I need a flyer that I can hand out to potential clients that describes the services that I offer. I am attaching an info sheet that has the information on the services I offer. (One exception is that I no longer offer the remote dietitian services listed on the flyer) . I am also including a file with my logo. I would like this flyer to hand out at conferences where I meet people that might not be familiar with my business or who are not knowledgeable of how my services might benefit them. The most important service that I offer is the data abstraction subcontracting. I will provide a PPT that will provide further info on this service.

Target Market(s)

Bariatric program directors and surgeons

Industry/Entity Type

Healthcare

Font styles to use
Serif
Sans Serif

Colors

Designer to choose colors to be used in the design.

Requirements
Must have
• a description of the services I offer
• how subcontracting will benefit them and save them money
• something noting my experience as I am one of the most experienced professionals in this field of bariatric surgery accreditation
Nice to have
• I am not a designer and created the flyer that I have provided. I realize it is not very professional and would like something that looks fresh and professional.
Should not have
• I don't want it to be too wordy and yet it needs to have a description of services offered. I want to include the yellow in my logo, but the flyer sample I have given you has waaaaay too much yellow and want to tone that down!

```html
<!DOCTYPE html>
<html lang="en">
<head>
<meta charset="utf-8">
<title>Marla Quinlan Consulting – Services Flyer</title>
<link rel="stylesheet" href="https://fonts.googleapis.com/css2?family=Montserrat:wght@500;600;700;800&family=Open+Sans:ital,wght@0,400;0,600;0,700;1,600&display=swap">
<style>
  :root {
    --yellow: #f7cf1d;
    --yellow-deep: #f2c10f;
    --ink: #2b2b2d;
    --charcoal: #333336;
    --charcoal-dark: #242426;
    --grey-text: #4a4a4a;
    --soft-text: #cfcfd2;
    --panel: #efefef;
    --rule: #d6d6d6;
    --white: #ffffff;
  }
  * { margin: 0; padding: 0; box-sizing: border-box; }
  html, body { width: 903px; height: 1200px; overflow: hidden; background: #e6e6e6; }
  .flyer {
    position: relative; width: 903px; height: 1200px; overflow: hidden;
    background: var(--white);
    font-family: "Open Sans", Arial, sans-serif; color: var(--grey-text);
  }

  /* Brand */
  .brand {
    position: absolute; left: 150px; top: 44px; height: 66px;
    display: flex; align-items: center; gap: 14px;
  }
  .brand__mark { width: 30px; height: 30px; background: var(--yellow); }
  .brand__name {
    font-family: "Montserrat", Arial, sans-serif; font-weight: 800;
    font-size: 36px; letter-spacing: 0.5px; color: var(--ink); text-transform: uppercase;
  }

  /* Hero */
  .hero { position: absolute; left: 0; top: 128px; width: 903px; height: 367px; }
  .hero__panel { position: absolute; left: 0; top: 0; width: 448px; height: 100%; background: var(--charcoal-dark); }
  .hero__accent { position: absolute; left: 0; top: 0; width: 10px; height: 100%; background: var(--yellow); }
  .hero__photo {
    position: absolute; left: 448px; top: 0; width: 455px; height: 100%;
    background: linear-gradient(135deg, #eef2f4 0%, #d9e2e6 45%, #c7cdd0 70%, #b08a66 100%);
  }
  .hero__title {
    position: absolute; left: 35px; top: 52px;
    font-family: "Montserrat", Arial, sans-serif; font-weight: 800;
    color: var(--white); text-transform: uppercase; line-height: 1;
  }
  .hero__line { display: block; font-size: 47px; letter-spacing: 0.5px; }
  .hero__line--big { font-size: 60px; margin-top: 6px; }
  .hero__tag {
    position: absolute; left: 35px; top: 178px; width: 378px; height: 78px;
    background: var(--yellow); color: var(--ink);
    font-family: "Montserrat", Arial, sans-serif; font-weight: 800; font-size: 50px;
    display: flex; align-items: center; justify-content: center; letter-spacing: 2px;
  }
  .hero__experience {
    position: absolute; left: 35px; top: 280px; width: 385px;
    font-size: 14.5px; line-height: 1.45; color: var(--soft-text);
  }
  .hero__experience strong { color: var(--white); font-weight: 700; }

  /* Services */
  .services-bar {
    position: absolute; left: 0; top: 495px; width: 903px; height: 58px;
    background: var(--charcoal); color: var(--white);
    font-family: "Montserrat", Arial, sans-serif; font-weight: 700; font-size: 19px;
    display: flex; align-items: center; justify-content: center; letter-spacing: 0.5px;
    border-bottom: 3px solid var(--yellow);
  }
  .services {
    position: absolute; left: 0; top: 553px; width: 903px; height: 464px;
    background: var(--panel);
  }
  .service { position: absolute; top: 16px; }
  .service__label {
    height: 34px; color: var(--ink); border-left: 5px solid var(--yellow);
    font-family: "Montserrat", Arial, sans-serif; font-weight: 700; font-size: 12.5px;
    display: flex; flex-direction: column; justify-content: center; padding: 0 8px;
    text-transform: uppercase; line-height: 1.15; background: var(--white);
  }
  .service__label small { font-size: 7.5px; font-weight: 600; }
  .service__text { margin-top: 16px; font-size: 13px; line-height: 1.45; color: var(--grey-text); }
  .service--assessment { left: 28px; width: 190px; }
  .service--development { left: 246px; width: 204px; }
  .service--staffing { left: 472px; width: 190px; }
  .service--inspection { left: 690px; width: 190px; }

  .savings {
    position: absolute; left: 28px; top: 372px; width: 847px; height: 78px;
    border-top: 1px solid var(--rule); padding-top: 12px;
    display: flex; gap: 22px; align-items: flex-start;
  }
  .savings__title {
    flex: none; width: 196px;
    font-family: "Montserrat", Arial, sans-serif; font-weight: 800; font-size: 15px;
    color: var(--ink); text-transform: uppercase; line-height: 1.25;
  }
  .savings__title span { display: block; width: 34px; height: 3px; background: var(--yellow); margin-top: 8px; }
  .savings__text { font-size: 13px; line-height: 1.5; color: var(--grey-text); }
  .savings__text strong { color: var(--ink); }

  /* Footer */
  .footer {
    position: absolute; left: 0; top: 1017px; width: 903px; height: 171px;
    background: var(--charcoal-dark); color: var(--white);
  }
  .footer__divider { position: absolute; left: 373px; top: 16px; width: 1px; height: 138px; background: #4a4a4d; }
  .why { position: absolute; left: 28px; top: 14px; width: 330px; }
  .why__title { font-family: "Montserrat", Arial, sans-serif; font-weight: 700; font-size: 19px; }
  .why__intro { margin-top: 8px; font-size: 9px; font-style: italic; font-weight: 600; color: var(--yellow); }
  .why__list { list-style: none; margin-top: 3px; font-size: 8.6px; font-style: italic; font-weight: 600; line-height: 1.38; }
  .why__list li::before { content: "\25CF\00a0"; font-size: 6px; vertical-align: 1px; }

  .contact { position: absolute; left: 414px; top: 20px; }
  .contact__title { font-family: "Montserrat", Arial, sans-serif; font-weight: 700; font-size: 15.5px; color: var(--yellow); text-transform: uppercase; }
  .contact__list { list-style: none; margin-top: 18px; }
  .contact__item {
    display: flex; align-items: center; gap: 10px; height: 26px;
    font-family: "Montserrat", Arial, sans-serif; font-weight: 700; font-size: 14px;
  }
  .contact__icon { width: 14px; height: 14px; flex: none; }

  .footer-stripe { position: absolute; left: 0; top: 1188px; width: 903px; height: 12px; background: var(--yellow-deep); }
</style>
</head>
<body>
<main class="flyer">

  <header class="brand">
    <span class="brand__mark" aria-hidden="true"></span>
    <span class="brand__name">Marla Quinlan Consulting</span>
  </header>

  <section class="hero">
    <div class="hero__panel"></div>
    <div class="hero__accent"></div>
    <div class="hero__photo" role="img" aria-label="Photo of a doctor in a white coat taking notes while speaking with a patient"></div>
    <h1 class="hero__title">
      <span class="hero__line">Helping You</span>
      <span class="hero__line hero__line--big">Navigate</span>
    </h1>
    <div class="hero__tag">BARIQAP</div>
    <p class="hero__experience"><strong>One of the most experienced professionals</strong> in bariatric surgery accreditation, guiding programs from first application to successful site survey.</p>
  </section>

  <h2 class="services-bar">OUR SERVICES</h2>

  <section class="services">
    <article class="service service--assessment">
      <h3 class="service__label">Program Assessment:</h3>
      <p class="service__text">A 2-day on-site assessment of your bariatric program covering bariqap compliance, best practice, business strategy and outcomes data collection, followed by a written report with solutions, timelines and opportunities for improvement.</p>
    </article>
    <article class="service service--development">
      <h3 class="service__label">Program Development–<small>Remote assistance and on-site:</small></h3>
      <p class="service__text">For centers developing a new program: guidance on policies and procedures, job descriptions, clinical pathways and protocols to ensure accreditation and bariqap compliance. The remote option includes regularly scheduled staff webinars.</p>
    </article>
    <article class="service service--staffing">
      <h3 class="service__label">BSCR Staffing:</h3>
      <p class="service__text">Subcontracted data abstraction that keeps you compliant. Your abstractor joins your team, leads qi projects, performs routine quality audits on data and attends all bariatric team meetings.</p>
    </article>
    <article class="service service--inspection">
      <h3 class="service__label">Mock Site Inspections:</h3>
      <p class="service__text">A rigorous one-day evaluation of accreditation readiness, with a critical assessment of every area in the bariqap standards. It closely mirrors the bariqap site survey process.</p>
    </article>

    <div class="savings">
      <h2 class="savings__title">Why subcontract your BSCR?<span></span></h2>
      <p class="savings__text"><strong>Save on salary, benefits, training and recertification costs.</strong> You pay only for the abstraction your case volume needs, with no coverage gaps during vacations or turnover, while an expert keeps your registry data accurate and survey-ready.</p>
    </div>
  </section>

  <footer class="footer">
    <section class="why">
      <h2 class="why__title">Why do we need BSCR?</h2>
      <p class="why__intro">The Standard states:</p>
      <ul class="why__list">
        <li>Each center is required to provide an BSCR to enter data into the BARIQAP registry</li>
        <li>BSCR should not be supervising patient care</li>
        <li>Must be able to fulfill case abstraction duties</li>
        <li>Must be able to complete ongoing training and recertification requirements</li>
        <li>Must be able to retrieve and enter long-term follow-up data on a compounding number of patients over time</li>
        <li>Must be able to fulfill requests for patient data and reports</li>
      </ul>
    </section>
    <div class="footer__divider"></div>
    <section class="contact">
      <h2 class="contact__title">Contact us for more information:</h2>
      <ul class="contact__list">
        <li class="contact__item">
          <svg class="contact__icon" viewBox="0 0 14 14" aria-hidden="true"><circle cx="7" cy="4" r="3" fill="#f7cf1d"/><path d="M1 14c0-4 3-6 6-6s6 2 6 6z" fill="#f7cf1d"/></svg>
          Marla Quinlan, RN, CBN Bariatric Program Consultant
        </li>
        <li class="contact__item">
          <svg class="contact__icon" viewBox="0 0 14 14" aria-hidden="true"><circle cx="7" cy="7" r="6" fill="none" stroke="#f7cf1d" stroke-width="1.5"/><path d="M4.5 4h1.5l.7 1.7-.9.7a4 4 0 0 0 1.8 1.8l.7-.9 1.7.7V9.5A1 1 0 0 1 9 10.5 5.5 5.5 0 0 1 3.5 5 1 1 0 0 1 4.5 4z" fill="#f7cf1d"/></svg>
          555-014-2290
        </li>
        <li class="contact__item">
          <svg class="contact__icon" viewBox="0 0 14 14" aria-hidden="true"><rect x="1" y="3" width="12" height="8" fill="#f7cf1d"/><path d="M1 3l6 5 6-5" fill="none" stroke="#242426" stroke-width="1.2"/></svg>
          marla@quinlanconsultgroup.com
        </li>
        <li class="contact__item">
          <svg class="contact__icon" viewBox="0 0 14 14" aria-hidden="true"><circle cx="7" cy="7" r="6" fill="#f7cf1d"/><path d="M1 7h12M7 1c-3 3-3 9 0 12M7 1c3 3 3 9 0 12" fill="none" stroke="#242426" stroke-width="1"/></svg>
          www.quinlanconsultgroup.com
        </li>
      </ul>
    </section>
  </footer>
  <div class="footer-stripe"></div>

</main>
</body>
</html>
```